Olive Oil Label Needs Graphic Designs

We need two sister label designs for 500ml bottles for our new brand "Casa Lumen". Casa Lumen is a high-end olive oil from Baeza, Spain which will be sold in the US. The oil will be produced from both Arbequina olives and Picual olives. Therefore, envisioning the same design just a different color scheme for the different labels.
The label should have the following characteristics; clean and simple, stand-out from mainstream labels, be eye-catching, give perception of high-end / high-quality.
Our current thinking of what we want (but please let your creative juices flow); lighter background, to be more eye catching, graphics of and olive, a olive branch or olive tree.
Text which should appear on the label are (not necessarily in this order);
Casa Lumen
Extra Virgin Olive Oil
Family Reserve
Arbequina (One design)
Picual (Second design)
The label should be about 3 inches wide and 5.5 inches in height.

```html
<!DOCTYPE html>
<html lang="en">
<head>
<meta charset="utf-8">
<title>Casa Lumen – Label Set</title>
<link href="https://fonts.googleapis.com/css2?family=EB+Garamond:wght@400;600;700&family=Kaushan+Script&display=swap" rel="stylesheet">
<style>
  :root {
    --paper: #ffffff;
    --ink: #1c1c1c;
    --rule: #555555;
    --plum: #7a2550;
    --plum-soft: #d9bccb;
    --violet: #5a4a7a;
    --violet-soft: #cfc8dc;
    --leaf: #6f8f3a;
    --leaf-soft: #dfe8cf;
  }
  * { box-sizing: border-box; margin: 0; padding: 0; }
  html, body { width: 1200px; height: 1200px; overflow: hidden; background: var(--paper); }
  body { position: relative; font-family: "EB Garamond", Georgia, serif; color: var(--ink); }

  .front-label, .back-label, .business-card {
    position: absolute; background: var(--paper); border: 1.5px solid var(--rule); overflow: hidden;
  }
  .front-label--picual { left: 80px; top: 60px; width: 322px; height: 596px; }
  .front-label--arbequina { left: 446px; top: 54px; width: 324px; height: 594px; }
  .back-label { left: 818px; top: 146px; width: 321px; height: 585px; padding: 24px 30px; text-align: center; }
  .business-card { left: 746px; top: 760px; width: 377px; height: 215px; }

  .brand-name { font-weight: 600; color: var(--ink); line-height: 1; white-space: nowrap; }
  .front-label .brand-name { position: absolute; left: 0; right: 0; top: 58px; text-align: center; font-size: 56px; }
  .product-type { position: absolute; left: 0; right: 0; top: 132px; text-align: center; font-size: 21px; }
  .reserve { position: absolute; left: 0; right: 0; top: 174px; text-align: center; font-family: "Kaushan Script", cursive; font-size: 19px; }
  .variety { position: absolute; right: 58px; bottom: 62px; font-size: 20px; font-weight: 700; }
  .front-label--arbequina .variety { right: 40px; bottom: 58px; }
  .net-weight { position: absolute; right: 30px; bottom: 26px; font-size: 13.5px; }
  .front-label--arbequina .net-weight { right: 22px; bottom: 30px; }

  .swoosh, .branch-art { position: absolute; }
  .swoosh { left: 0; top: 0; width: 100%; height: 100%; }
  .front-label--picual .branch-art { left: 0; top: 290px; width: 322px; height: 300px;
    background: radial-gradient(closest-side at 45% 55%, #5a1e2c 0%, #6e7d35 40%, rgba(120,150,70,.35) 75%, rgba(255,255,255,0) 100%); }
  .front-label--arbequina .branch-art { left: 0; top: 250px; width: 260px; height: 344px;
    background: radial-gradient(closest-side at 45% 50%, #33244f 0%, #6d8a3e 42%, rgba(120,150,70,.35) 75%, rgba(255,255,255,0) 100%); }

  .back-label .brand-name { font-size: 36px; margin-bottom: 10px; }
  .story { font-size: 13.5px; line-height: 1.18; }
  .divider { display: block; margin: 8px auto 4px; }
  .facts-title { font-family: "Kaushan Script", cursive; font-size: 15px; }
  .serving { font-size: 12.5px; line-height: 1.2; margin-bottom: 6px; }
  .facts { border: 1.5px solid var(--ink); margin: 0 6px; padding: 5px 8px; text-align: left; font-size: 11px; font-weight: 700; line-height: 1.2; }
  .facts table { width: 100%; border-collapse: collapse; }
  .facts td { padding: 0; border-bottom: 1px solid var(--ink); }
  .facts td.pct { text-align: left; width: 58px; }
  .facts .indent { padding-left: 12px; }
  .facts .note { font-size: 10.5px; margin-top: 3px; }
  .footnote { font-size: 11px; line-height: 1.15; margin: 6px 30px; }
  .allergen { font-size: 12px; line-height: 1.15; }

  .business-card .card-art { position: absolute; left: 0; top: 0; width: 140px; height: 215px;
    background: radial-gradient(closest-side at 40% 55%, #3a2a55 0%, #6f8f3a 42%, rgba(150,175,100,.35) 75%, rgba(255,255,255,0) 100%); }
  .business-card .brand-name { position: absolute; left: 150px; top: 30px; font-size: 40px; }
  .tagline { position: absolute; left: 150px; top: 100px; font-size: 14px; font-weight: 700; line-height: 1.2; }
  .contact { position: absolute; right: 28px; top: 160px; font-size: 13px; font-weight: 700; line-height: 1.25; text-align: left; }
</style>
</head>
<body>

<section class="front-label front-label--picual">
  <svg class="swoosh" viewBox="0 0 322 596" aria-hidden="true">
    <defs><linearGradient id="plum-fade" x1="0" y1="1" x2="1" y2="0">
      <stop offset="0" stop-color="var(--plum)"/><stop offset="0.6" stop-color="var(--plum-soft)"/><stop offset="1" stop-color="#fff" stop-opacity="0"/></linearGradient></defs>
    <path d="M0 300 C120 390 230 470 322 596 L0 596 Z" fill="url(#plum-fade)"/>
  </svg>
  <div class="branch-art" role="img" aria-label="Illustrated olive branch with dark red Picual olives"></div>
  <div class="brand-name">Casa Lumen</div>
  <div class="product-type">Extra Virgin Olive oil</div>
  <div class="reserve">Family Reserve</div>
  <div class="variety">Picual</div>
  <div class="net-weight">Net wt. 00 oz (000 ml)</div>
</section>

<section class="front-label front-label--arbequina">
  <svg class="swoosh" viewBox="0 0 324 594" aria-hidden="true">
    <defs><linearGradient id="violet-fade" x1="0" y1="0.6" x2="1" y2="0.9">
      <stop offset="0" stop-color="var(--violet)"/><stop offset="0.7" stop-color="var(--violet-soft)"/><stop offset="1" stop-color="#fff"/></linearGradient></defs>
    <path d="M0 330 C110 400 220 420 324 500 L324 594 L0 594 Z" fill="url(#violet-fade)"/>
  </svg>
  <div class="branch-art" role="img" aria-label="Illustrated olive branch with purple Arbequina olives"></div>
  <div class="brand-name">Casa Lumen</div>
  <div class="product-type">Extra Virgin Olive oil</div>
  <div class="reserve">Family Reserve</div>
  <div class="variety">Arbequina</div>
  <div class="net-weight">Net wt. 00 oz (000 ml)</div>
</section>

<section class="back-label">
  <div class="brand-name">Casa Lumen</div>
  <p class="story">We deliver a high quality extra virgin olive oil from one of the finest provinces in Spain. We have generations of caring for our trees and harvesting from our family reserve. We have two types of trees which generate a distinct olive oil, Arbequina and Picual.</p>
  <svg class="divider" width="90" height="8" viewBox="0 0 90 8" aria-hidden="true"><path d="M2 6 Q45 -2 88 6" fill="none" stroke="var(--ink)" stroke-width="1.2"/></svg>
  <div class="facts-title">Nutrition Facts</div>
  <p class="serving">Serving Size 1 Tbsp. (15 ml)<br>Servings per Container - 33</p>
  <div class="facts">
    <table>
      <tr><td colspan="2">Amount Per Serving</td></tr>
      <tr><td colspan="2">Calories 120</td></tr>
      <tr><td colspan="2">Calories from Fat 120</td></tr>
      <tr><td colspan="2">% Daily value*</td></tr>
      <tr><td>Total Fat 2 g</td><td class="pct">22%</td></tr>
      <tr><td class="indent">Saturated Fat 2 g</td><td class="pct">10%</td></tr>
      <tr><td class="indent" colspan="2">Trans Fat 0 g</td></tr>
      <tr><td>Cholesterol 0 mg</td><td class="pct">0%</td></tr>
      <tr><td>Sodium 0 g</td><td class="pct">0%</td></tr>
      <tr><td>Total Carbohydrate 0 g</td><td class="pct">0%</td></tr>
      <tr><td colspan="2">Sugar 0 g</td></tr>
      <tr><td colspan="2">Protein 0 g</td></tr>
    </table>
    <p class="note">Not a significant source of dietary fiber, Vitamin A, Vitamin C, Calcium or Iron.</p>
  </div>
  <p class="footnote">*Percent Daily Values are based on a 2,000 calorie diet.</p>
  <p class="allergen">This product has been produced free of soy, wheat, gluten, nuts, peanuts, dairy, and genetically engineered ingredients.</p>
</section>

<section class="business-card">
  <svg class="swoosh" viewBox="0 0 377 215" aria-hidden="true">
    <defs><linearGradient id="leaf-fade" x1="0" y1="1" x2="1" y2="0">
      <stop offset="0" stop-color="var(--leaf)"/><stop offset="0.55" stop-color="var(--leaf-soft)"/><stop offset="1" stop-color="#fff"/></linearGradient></defs>
    <path d="M0 0 L130 0 C150 80 230 160 377 215 L0 215 Z" fill="url(#leaf-fade)" opacity="0.8"/>
  </svg>
  <div class="card-art" role="img" aria-label="Illustrated olive branch with purple olives"></div>
  <div class="brand-name">Casa Lumen</div>
  <p class="tagline">High Quality, Family Reserve<br>Olive Oils from Baeza, Spain</p>
  <p class="contact">(Contact Info)<br>www.casalumen.com</p>
</section>

</body>
</html>
```